Design the Mobile Version of Existing Web Based Health Platform

Loomcrest is a social business enterprise that focus on public health by applying innovative healthcare services and consumer internet technology. Loomcrest offers a personalized platform of health promotion and disease prevention that puts the individual back in control of his life.

Loomcrest is looking for a Mobile Web UX/Visual Design professional to create a mobile version of Loomcrest website platform for iPhone, iPad/tablet and Android.

Contestants must to check www.loomcrest-demo.com.br to have a better understanding of Loomcrest Platform by creating an account (it's in portuguese, but anyone can get the general idea).

The mobile version of Loomcrest should have very similar functionality and user flows. This job is not to reengineer or re-imagine Loomcrest. It is just to reformat the existing functionality so it works well on mobile devices.

This description below is to help you to understand the core features of the platform (check the attachments to see the new web design of each one):

- Personally Controlled Health Record - PCHR enables an individual to own and manage a complete, secure, digital copy of her health and wellness information.
- Health Risk Assessments - is a process to estimate the nature and probability of adverse health effects, based on personal and family historical data, behavior and environment.
- Simulation of future health - "what if analysis" that emphasizes health education and behavior change.
- Step Quests - a program that gives you the opportunity to the participant to advance his personal well-being by doing simple Step Quests
- Health Alerts and Recommendations and Missing Data - Recommendations based on Wellbeing Bureau Guidelines and Federal Wellness Review Panel (FWRP), plus notifications to update outdated information.

The deliverable for this project is a psd file with a designed mobile version of Loomcrest.

A new design of the web platform is under construction. You can also check it looking at the files attached.

Target Market(s)

people 25-40 years old, 60% female, socially engaged

Industry/Entity Type

Healthcare

Requirements
Must have
• iPhone, iPad and Android version

Design must cover all current functionalities available on the web version (please, ensure you understand all features by creating an account at www.loomcrest-demo.com.br)

- Login/Sign up
- Welcome (first assessment)
- Add to Personal Controlled Health Record (PCHR)
- Update/Remove PCHR
- List PCHR
- Riskgrid (risk assessmen results)
- Simulation
- Alerts
- Missing data
- Recommendations
- StepQuest
- Badges
- Configurations

It's important to check the attachments to see how the web platform design is evolving.

```html
<!DOCTYPE html>
<html lang="en">
<head>
<meta charset="utf-8">
<title>Loomcrest – Simulation</title>
<link href="https://fonts.googleapis.com/css2?family=Arimo:ital,wght@0,400;0,700;1,400;1,700&display=swap" rel="stylesheet">
<style>
  :root{
    --orange:#f7923a;
    --orange-dark:#e0701c;
    --orange-light:#fbb063;
    --yellow:#ffd45a;
    --ink-grey:#a9a9a9;
    --label-grey:#b5b5b5;
    --line:#d6d6d6;
    --bg:#ededed;
    --white:#ffffff;
    --black:#000000;
    --red:#ee1c1c;
    --amber:#ffa200;
    --gold:#ffd800;
    --lime:#9acd32;
    --olive:#5f8a1e;
    --pre:#f08a3c;
  }
  *{box-sizing:border-box;margin:0;padding:0}
  html,body{width:800px;height:1200px;overflow:hidden;background:var(--bg)}
  body{font-family:"Arimo",Arial,sans-serif}
  .screen{position:absolute;left:0;top:0;width:640px;height:960px;transform:scale(1.25);transform-origin:0 0;
    background:linear-gradient(#e9e9e9,#f7f7f7 40%,#ebebeb);overflow:hidden}
  .status-bar{position:absolute;left:0;top:0;width:640px;height:40px;background:linear-gradient(#3a3a3a,#000);color:var(--white)}
  .carrier{position:absolute;left:52px;top:12px;font-size:16px;font-weight:700;letter-spacing:.5px}
  .signal{position:absolute;left:10px;top:12px}
  .lock{position:absolute;left:310px;top:8px}
  .battery{position:absolute;left:592px;top:11px}
  .app-header{position:absolute;left:0;top:40px;width:640px;height:85px;
    background:linear-gradient(#fbb060,#f58a24 55%,#ef7a14);border-bottom:1px solid #d9660c}
  .back-button{position:absolute;left:22px;top:16px}
  .back-label{position:absolute;left:54px;top:32px;font-size:20px;font-weight:700;color:#8a4a00}
  .page-title{position:absolute;left:0;width:630px;top:16px;text-align:center;font-size:42px;font-weight:700;color:var(--white);
    text-shadow:0 1px 2px rgba(0,0,0,.25)}
  .search{position:absolute;left:22px;top:141px;width:357px;height:51px;background:var(--white);border:1px solid var(--line);border-radius:6px}
  .search svg{position:absolute;right:14px;top:16px}
  .avatar{position:absolute;left:405px;top:137px;width:59px;height:56px;border:2px solid #ccc;border-radius:4px;
    background:linear-gradient(#6d8fa8,#4d5a4e 60%,#2d3a34)}
  .greeting{position:absolute;left:481px;top:145px;font-style:italic;font-size:16px;color:var(--ink-grey)}
  .user-name{position:absolute;left:480px;top:164px;font-style:italic;font-weight:700;font-size:20px;color:var(--orange-dark)}
  .side-nav{position:absolute;left:0;top:215px;width:73px;height:306px;background:var(--white);border-radius:0 6px 6px 0;
    box-shadow:1px 1px 4px rgba(0,0,0,.2)}
  .side-nav li{list-style:none;height:51px;border-bottom:1px solid #e2e2e2;display:flex;align-items:center;justify-content:center}
  .side-nav li.active{background:#f4f4f4}
  .tabs{position:absolute;left:90px;top:215px;width:537px;height:51px;border:1px solid var(--line);border-radius:6px;display:flex;overflow:hidden}
  .tab{flex:1;display:flex;align-items:center;justify-content:center;font-size:18px;font-weight:700}
  .tab.active{background:linear-gradient(#fff,#f3f3f3);color:var(--orange)}
  .tab.inactive{background:linear-gradient(#f2f2f2,#e4e4e4);color:#c4c4c4;border-left:1px solid var(--line)}
  .body-figure{position:absolute;left:122px;top:290px;width:104px;height:322px;border-radius:40px 40px 10px 10px;
    background:linear-gradient(#fde3cc,#fbd3b0)}
  .legend{position:absolute;left:30px;top:621px;list-style:none}
  .legend li{height:25.5px;font-size:13px;color:#777;display:flex;align-items:center}
  .legend i{width:11px;height:11px;border-radius:50%;margin-right:9px;display:inline-block}
  .field{position:absolute;left:250px;width:374px;height:31px}
  .field .label{position:absolute;right:224px;top:6px;font-size:15px;font-weight:700;color:var(--label-grey);white-space:nowrap}
  .field .icon{position:absolute;left:160px;top:-4px;width:36px;height:36px;border-radius:6px;background:#c9c9c9;opacity:.7}
  .field .input{position:absolute;left:207px;top:0;width:167px;height:31px;background:var(--white);border:1px solid var(--line);border-radius:3px}
  .field .unit{position:absolute;right:30px;top:8px;font-size:12px;color:#999}
  .field .input svg{position:absolute;right:8px;top:11px}
  .action{position:absolute;height:32px;background:linear-gradient(var(--orange-light),var(--orange));border:1px solid var(--orange-dark);
    color:var(--white);font-size:14px;font-weight:700;display:flex;align-items:center;justify-content:center}
  .risks{position:absolute;left:25px;top:797px;list-style:none}
  .risks li{height:37.5px;display:flex;align-items:center;font-size:15px;font-weight:700;color:#9a9a9a}
  .risks i{width:19px;height:30px;background:#c5c5c5;border-radius:4px 0 0 4px;margin-right:13px;display:inline-block}
</style>
</head>
<body>
<div class="screen">
  <div class="status-bar">
    <svg class="signal" width="38" height="16" viewBox="0 0 38 16"><g fill="#fff">
      <rect x="0" y="12" width="4" height="4"/><rect x="7" y="9" width="4" height="7"/><rect x="14" y="6" width="4" height="10"/>
      <rect x="21" y="3" width="4" height="13"/><rect x="28" y="0" width="4" height="16"/></g></svg>
    <span class="carrier">NOVACELL 3G</span>
    <svg class="lock" width="20" height="24" viewBox="0 0 20 24"><path d="M5 10V7a5 5 0 0 1 10 0v3" fill="none" stroke="#ccc" stroke-width="2.5"/><rect x="1" y="10" width="18" height="13" rx="2" fill="#ccc"/></svg>
    <svg class="battery" width="38" height="18" viewBox="0 0 38 18"><rect x="1" y="1" width="32" height="16" rx="2" fill="none" stroke="#fff" stroke-width="2"/><rect x="4" y="4" width="26" height="10" fill="#fff"/><rect x="34" y="6" width="3" height="6" fill="#fff"/></svg>
  </div>

  <header class="app-header">
    <svg class="back-button" width="102" height="52" viewBox="0 0 102 52">
      <defs><linearGradient id="backFill" x1="0" y1="0" x2="0" y2="1"><stop offset="0" stop-color="#ffe98a"/><stop offset="1" stop-color="#f7b823"/></linearGradient></defs>
      <path d="M2 26 L24 2 H96 a4 4 0 0 1 4 4 V46 a4 4 0 0 1-4 4 H24 Z" fill="url(#backFill)" stroke="#c98308" stroke-width="1.5"/>
    </svg>
    <span class="back-label">Back</span>
    <h1 class="page-title">Simulation</h1>
  </header>

  <div class="search">
    <svg width="16" height="16" viewBox="0 0 16 16"><circle cx="6.5" cy="6.5" r="4.8" fill="none" stroke="#999" stroke-width="2.2"/><path d="M10 10l4.5 4.5" stroke="#999" stroke-width="2.6" stroke-linecap="round"/></svg>
  </div>
  <div class="avatar" role="img" aria-label="User profile photo"></div>
  <p class="greeting">Good day,</p>
  <p class="user-name">Marilu !</p>

  <ul class="side-nav">
    <li><svg width="22" height="36" viewBox="0 0 22 36"><circle cx="11" cy="7" r="6" fill="#bbb"/><rect x="2" y="15" width="18" height="20" rx="8" fill="#bbb"/></svg></li>
    <li class="active"><svg width="26" height="36" viewBox="0 0 26 36"><circle cx="13" cy="6" r="5" fill="var(--orange)"/><rect x="3" y="13" width="20" height="22" rx="3" fill="none" stroke="var(--orange)" stroke-width="2.5"/></svg></li>
    <li><svg width="32" height="30" viewBox="0 0 32 30"><rect x="1" y="2" width="20" height="15" rx="7" fill="none" stroke="#bbb" stroke-width="2"/><rect x="11" y="12" width="20" height="15" rx="7" fill="none" stroke="#bbb" stroke-width="2"/></svg></li>
    <li><svg width="26" height="32" viewBox="0 0 26 32"><rect x="3" y="1" width="21" height="30" rx="2" fill="#bbb"/><g stroke="#fff" stroke-width="2"><path d="M0 7h6M0 14h6M0 21h6"/></g></svg></li>
    <li><svg width="28" height="30" viewBox="0 0 28 30"><path d="M4 2h20v8a10 10 0 0 1-20 0z" fill="none" stroke="#bbb" stroke-width="2"/><path d="M14 20v5M8 28h12" stroke="#bbb" stroke-width="2.5"/></svg></li>
    <li><svg width="28" height="28" viewBox="0 0 28 28"><g fill="#bbb"><rect x="0" y="0" width="7" height="7"/><rect x="10" y="0" width="7" height="7"/><rect x="20" y="0" width="7" height="7"/><rect x="0" y="10" width="7" height="7"/><rect x="10" y="10" width="7" height="7"/><rect x="20" y="10" width="7" height="7"/><rect x="0" y="20" width="7" height="7"/><rect x="10" y="20" width="7" height="7"/><rect x="20" y="20" width="7" height="7"/></g></svg></li>
  </ul>

  <nav class="tabs">
    <div class="tab active">Simulation</div>
    <div class="tab inactive">My goal</div>
  </nav>

  <div class="body-figure" role="img" aria-label="Outline of a human body with highlighted risk areas"></div>

  <ul class="legend">
    <li><i style="background:var(--pre)"></i>Condição pré-existente</li>
    <li><i style="background:var(--red)"></i>Alto</li>
    <li><i style="background:var(--amber)"></i>Acima da Média</li>
    <li><i style="background:var(--gold)"></i>Na Média</li>
    <li><i style="background:var(--lime)"></i>Abaixo da Média</li>
    <li><i style="background:var(--olive)"></i>Baixo</li>
  </ul>

  <div class="field" style="top:309px"><span class="label">Height</span><span class="icon" role="img" aria-label="Scale icon"></span><div class="input"><span class="unit">Kg</span><svg width="12" height="9"><path d="M0 0h12L6 9z" fill="#999"/></svg></div></div>
  <div class="field" style="top:358px"><span class="label">Physical activity</span><span class="icon" role="img" aria-label="Arm muscle icon"></span><div class="input"><span class="unit">/ week</span><svg width="12" height="9"><path d="M0 0h12L6 9z" fill="#999"/></svg></div></div>
  <div class="field" style="top:409px"><span class="label">Cigarettes</span><span class="icon" role="img" aria-label="Cigarette icon"></span><div class="input"><span class="unit">/ day</span><svg width="12" height="9"><path d="M0 0h12L6 9z" fill="#999"/></svg></div></div>
  <div class="field" style="top:459px"><span class="label" style="top:0">Total cholesterol</span><span class="icon" role="img" aria-label="Drop icon"></span><div class="input"><span class="unit">mg/dl</span><svg width="12" height="9"><path d="M0 0h12L6 9z" fill="#999"/></svg></div></div>
  <div class="field" style="top:510px"><span class="label" style="top:2px">Good cholesterol</span><span class="icon" role="img" aria-label="Test tube icon"></span><div class="input"><span class="unit">mg/dl</span><svg width="12" height="9"><path d="M0 0h12L6 9z" fill="#999"/></svg></div></div>
  <div class="field" style="top:562px"><span class="label">Glucose</span><span class="icon" role="img" aria-label="Sugar jar icon"></span><div class="input"><span class="unit">mg/dl</span><svg width="12" height="9"><path d="M0 0h12L6 9z" fill="#999"/></svg></div></div>
  <div class="field" style="top:614px"><span class="label">Waist</span><span class="icon" role="img" aria-label="Waist measure icon"></span><div class="input"><span class="unit">cm</span><svg width="12" height="9"><path d="M0 0h12L6 9z" fill="#999"/></svg></div></div>
  <div class="field" style="top:664px"><span class="label" style="top:17px">Breathing</span><span class="icon" role="img" aria-label="Lungs icon" style="top:12px"></span><div class="input"><span class="unit">mg/dl</span><svg width="12" height="9"><path d="M0 0h12L6 9z" fill="#999"/></svg></div></div>
  <div class="field" style="top:714px"><span class="label" style="top:13px">Pressure</span><span class="icon" role="img" aria-label="Blood pressure gauge icon"></span><div class="input"><span class="unit">mmhg</span><svg width="12" height="9"><path d="M0 0h12L6 9z" fill="#999"/></svg></div></div>

  <div class="action" style="left:457px;top:780px;width:162px">calculate</div>
  <div class="action" style="left:459px;top:835px;width:164px">set target</div>
  <div class="action" style="left:456px;top:890px;width:164px">clean</div>

  <ul class="risks">
    <li><i></i>Risco de arterial coronariana : 0,15%</li>
    <li><i></i>Risco de derrame cerebral : 0,25%</li>
    <li><i></i>Risco de cancer : 0,13%</li>
    <li><i></i>Risco de diabetes : 0,20%</li>
  </ul>
</div>
</body>
</html>
```